We're Hiring Poster or Flyer design

We’re Hiring Details:

Positions include:
Office Manager
Office Assistant
Data Entry Techs
Outreach Manager
Asst. Outreach Manager
Events Coordinator
Drivers (must have personal car, insurance & Driver’s License)
Outreach Specialist—Walkers
Outreach Specialist—Phone/Telemarketing (evenings only)

Excellent Pay ! Fun Atmosphere ! Bonus Pay with Promotional & Career Advancement Opportunities

***************
need 3 formats of SAME flyer:
1) 8.5 x 11
2) 8.5 x 14
3) 11 x17

creative and eye catching a must; this flyer will be used on college bulletin boards and used to attract a younger demographic . . hip and chic look with "Americana style or political motif" preferred.

Target Market(s)

younger demographic . . flyer will be used during college recruiting fairs and in younger settings---age BRACKET is 21 - 35 Years old

Industry/Entity Type

Employment Agency

Font styles to use
Sans Serif

Colors

Designer to choose colors to be used in the design.

Requirements
Must have
• clean and attractive; hip; chic; simple and with good stock pics and layout
Nice to have
• american flag and patriotism
Should not have
• too much details on the job -- I only included the job announcement so you can get an idea of WHAT and WHO I am looking for . . don't list all the BORING details on the flyer/poster

```html
<!DOCTYPE html>
<html lang="en">
<head>
<meta charset="utf-8">
<title>We're Hiring Flyer</title>
<link href="https://fonts.googleapis.com/css2?family=Encode+Sans+Semi+Condensed:wght@400;600;700&family=Roboto+Condensed:ital,wght@0,700;1,400&display=swap" rel="stylesheet">
<style>
  :root {
    --page-bg: #d4d5d7;
    --paper: #ffffff;
    --navy: #14336b;
    --navy-deep: #0c2556;
    --blue: #1d57a8;
    --red: #b8222a;
    --red-bright: #c8262d;
    --gray-text: #4a4a4a;
    --swoosh: #c9cbcf;
    --white: #ffffff;
  }
  * { margin: 0; padding: 0; box-sizing: border-box; }
  html, body {
    width: 986px; height: 1200px; overflow: hidden;
    background: var(--page-bg);
  }
  body { position: relative; font-family: "Encode Sans Semi Condensed", sans-serif; }

  .flyer {
    position: absolute; left: 80px; top: 15px;
    width: 827px; height: 1170px;
    background: var(--paper);
    overflow: hidden;
  }

  .team-photo {
    position: absolute; left: 0; top: 0; width: 827px; height: 470px;
    background: linear-gradient(180deg, #eef2f4 0%, #e4e8ea 35%, #cdb8a6 70%, #8c8f99 100%);
    clip-path: path('M0 0 H827 V400 Q414 480 0 405 Z');
    z-index: 2;
  }

  .flag-panel {
    position: absolute; left: 0; top: 400px; width: 470px; height: 700px;
    background:
      linear-gradient(170deg, rgba(32,44,120,0.95) 0%, rgba(60,66,140,0.85) 30%, rgba(170,168,196,0.75) 50%, rgba(150,30,45,0.9) 68%, rgba(215,210,225,0.8) 80%, rgba(170,25,35,0.9) 100%);
    clip-path: path('M0 0 H400 Q440 300 455 700 H0 Z');
    z-index: 1;
  }

  .decor { position: absolute; left: 0; top: 0; z-index: 3; pointer-events: none; }

  .footer-band {
    position: absolute; left: 0; top: 1055px; width: 827px; height: 115px;
    background: linear-gradient(90deg, var(--blue) 0%, var(--navy) 60%, var(--navy-deep) 100%);
    clip-path: path('M0 38 Q414 -14 827 38 V115 H0 Z');
    z-index: 4;
    color: var(--white); text-align: center;
  }
  .footer-band .headline { margin-top: 50px; font-size: 21px; font-weight: 700; }
  .footer-band .subline { font-size: 20px; font-weight: 400; margin-top: 2px; }

  .positions { position: absolute; left: 0; top: 528px; z-index: 5; }
  .positions-tag {
    width: 352px; height: 44px; line-height: 44px;
    background: var(--red-bright);
    border-radius: 0 22px 22px 0;
    color: var(--white); font-weight: 700; font-size: 24px;
    padding-left: 32px;
  }
  .positions-list { list-style: none; margin-top: 26px; padding-left: 38px; }
  .positions-list li {
    position: relative; padding-left: 35px;
    color: var(--white); font-size: 25px; line-height: 39.5px;
    width: 420px;
  }
  .positions-list li svg { position: absolute; left: 0; top: 11px; }

  .side-panel { position: absolute; left: 470px; top: 450px; width: 357px; z-index: 5; text-align: center; }
  .candidate-name {
    margin-top: 118px;
    display: flex; align-items: center; justify-content: center; gap: 10px;
    color: var(--navy); font-weight: 700; font-size: 30px; line-height: 1.15;
  }
  .candidate-name .mark { width: 16px; height: 16px; background: var(--navy); flex: none; }
  .hiring {
    margin-top: 58px;
    font-family: "Roboto Condensed", sans-serif; font-weight: 700;
    color: var(--red); font-size: 74px; line-height: 70px; letter-spacing: 2px;
  }
  .website { margin-top: 28px; color: var(--red); font-weight: 700; font-size: 21px; }
  .contact {
    margin-top: 22px;
    font-family: "Roboto Condensed", sans-serif; font-style: italic; font-weight: 400;
    color: var(--gray-text); font-size: 18px; line-height: 28px;
  }
</style>
</head>
<body>
  <main class="flyer">
    <div class="team-photo" role="img" aria-label="Group of young professionals in business attire standing in a bright office, some holding folders"></div>
    <div class="flag-panel" role="img" aria-label="Waving American flag with stars and red and white stripes"></div>

    <svg class="decor" width="827" height="1170" viewBox="0 0 827 1170">
      <path d="M0 405 Q414 480 827 400" fill="none" stroke="var(--swoosh)" stroke-width="7"/>
      <path d="M400 452 Q440 750 455 1100" fill="none" stroke="var(--swoosh)" stroke-width="6"/>
      <path d="M0 1088 Q414 1028 827 1088" fill="none" stroke="var(--swoosh)" stroke-width="14"/>
    </svg>

    <section class="positions">
      <div class="positions-tag">POSITIONS INCLUDE:</div>
      <ul class="positions-list">
        <li><svg width="20" height="20" viewBox="0 0 20 20"><circle cx="10" cy="10" r="9" fill="#fff"/><path d="M8 6l4 4-4 4" fill="none" stroke="#14336b" stroke-width="2.4"/></svg>Office Manager</li>
        <li><svg width="20" height="20" viewBox="0 0 20 20"><circle cx="10" cy="10" r="9" fill="#fff"/><path d="M8 6l4 4-4 4" fill="none" stroke="#14336b" stroke-width="2.4"/></svg>Office Assistant</li>
        <li><svg width="20" height="20" viewBox="0 0 20 20"><circle cx="10" cy="10" r="9" fill="#fff"/><path d="M8 6l4 4-4 4" fill="none" stroke="#14336b" stroke-width="2.4"/></svg>Data Entry Techs</li>
        <li><svg width="20" height="20" viewBox="0 0 20 20"><circle cx="10" cy="10" r="9" fill="#fff"/><path d="M8 6l4 4-4 4" fill="none" stroke="#14336b" stroke-width="2.4"/></svg>Outreach Manager</li>
        <li><svg width="20" height="20" viewBox="0 0 20 20"><circle cx="10" cy="10" r="9" fill="#fff"/><path d="M8 6l4 4-4 4" fill="none" stroke="#14336b" stroke-width="2.4"/></svg>Asst. Outreach Manager</li>
        <li><svg width="20" height="20" viewBox="0 0 20 20"><circle cx="10" cy="10" r="9" fill="#fff"/><path d="M8 6l4 4-4 4" fill="none" stroke="#14336b" stroke-width="2.4"/></svg>Events Coordinator</li>
        <li><svg width="20" height="20" viewBox="0 0 20 20"><circle cx="10" cy="10" r="9" fill="#fff"/><path d="M8 6l4 4-4 4" fill="none" stroke="#14336b" stroke-width="2.4"/></svg>Drivers (must have personal car, insurance &amp; Driver’s License)</li>
        <li><svg width="20" height="20" viewBox="0 0 20 20"><circle cx="10" cy="10" r="9" fill="#fff"/><path d="M8 6l4 4-4 4" fill="none" stroke="#14336b" stroke-width="2.4"/></svg>Outreach Specialist - Walkers</li>
        <li><svg width="20" height="20" viewBox="0 0 20 20"><circle cx="10" cy="10" r="9" fill="#fff"/><path d="M8 6l4 4-4 4" fill="none" stroke="#14336b" stroke-width="2.4"/></svg>Outreach Specialist - Phone/ Telemarketing (evenings only)</li>
      </ul>
    </section>

    <section class="side-panel">
      <div class="candidate-name"><span class="mark"></span><span>Daniel Moreno<br>for Mayor</span></div>
      <h1 class="hiring">WE'RE<br>HIRING</h1>
      <p class="website">www.MorenoForMayor.com</p>
      <p class="contact">Please email this job order to:<br>jobs.mfm2018@mailbox.com<br>Questions Call Alex Turner<br>at: (555) 014-2290</p>
    </section>

    <footer class="footer-band">
      <p class="headline">EXCELLENT PAY ! FUN ATMOSPHERE !</p>
      <p class="subline">Bonus Pay with Promotional &amp; Career Advancement Opportunities</p>
    </footer>
  </main>
</body>
</html>
```